Corvenix Business Card

Our mission is to craft high value solutions combining consulting and edge technologies for helping big and middle sized companies in the Digital Transformation Process that they must face. We think that this transformation will impact business processes and people skills in a new manner. Corvenix's value proposition is to collaborate with our clients for creating new competitive advantages based on technology, processes and people.
We already have a logo designed through your platform.

Industry/Entity Type

Business

```html
<!DOCTYPE html>
<html lang="en">
<head>
<meta charset="UTF-8">
<title>Corvenix Business Card</title>
<link rel="stylesheet" href="https://fonts.googleapis.com/css2?family=Michroma&family=Roboto:wght@400&display=swap">
<style>
  :root {
    --bg: #eceeef;
    --card: #fafafa;
    --ink: #161616;
    --band: #111111;
    --blue: #1b8fd2;
    --blue-light: #4fb6e8;
    --grey: #8a8a8a;
  }
  * { margin: 0; padding: 0; box-sizing: border-box; }
  html, body {
    width: 1200px;
    height: 1000px;
    overflow: hidden;
    background: var(--bg);
  }
  .canvas {
    position: relative;
    width: 1200px;
    height: 1000px;
  }
  .card {
    position: absolute;
    left: 250px;
    width: 700px;
    height: 400px;
    background: var(--card);
    overflow: hidden;
    box-shadow: 0 6px 18px rgba(0,0,0,0.12);
  }
  .card--back { top: 70px; }
  .card--front { top: 530px; }
  .card__bands {
    position: absolute;
    inset: 0;
    width: 700px;
    height: 400px;
  }
  .brand {
    position: absolute;
    display: flex;
    align-items: center;
    gap: 18px;
  }
  .brand__dot {
    border-radius: 50%;
    background: var(--blue);
  }
  .brand__name {
    font-family: "Michroma", sans-serif;
    color: var(--ink);
    letter-spacing: 2px;
  }
  .card--back .brand {
    left: 50%;
    top: 125px;
    transform: translateX(-50%);
  }
  .card--back .brand__dot { width: 78px; height: 78px; }
  .card--back .brand__name { font-size: 40px; }

  .card--front .brand { left: 48px; top: 42px; }
  .card--front .brand__dot { width: 58px; height: 58px; }
  .card--front .brand__name { font-size: 30px; }

  .person {
    position: absolute;
    left: 52px;
    top: 128px;
  }
  .person__name {
    font-family: "Michroma", sans-serif;
    font-size: 25px;
    color: var(--blue);
    line-height: 1.2;
  }
  .person__role {
    font-family: "Roboto", sans-serif;
    font-size: 16px;
    color: var(--ink);
    letter-spacing: 1px;
    margin-top: 2px;
  }
  .contact {
    position: absolute;
    right: 40px;
    top: 196px;
    list-style: none;
  }
  .contact__item {
    display: flex;
    justify-content: flex-end;
    align-items: center;
    gap: 16px;
    height: 26px;
    font-family: "Michroma", sans-serif;
    font-size: 16px;
    color: var(--ink);
    letter-spacing: 1px;
  }
  .contact__icon {
    width: 16px;
    height: 16px;
    flex: none;
  }
</style>
</head>
<body>
<main class="canvas">

  <section class="card card--back" aria-label="Business card back">
    <svg class="card__bands" viewBox="0 0 700 400" aria-hidden="true">
      <path d="M0 0 H700 V28 L0 12 Z" fill="var(--band)"/>
      <path d="M0 14 L700 30 V40 L0 24 Z" fill="var(--blue)"/>
      <path d="M0 290 L700 318 V326 L0 298 Z" fill="var(--blue-light)"/>
      <path d="M0 300 L700 328 V400 H0 Z" fill="var(--band)"/>
    </svg>
    <div class="brand">
      <span class="brand__dot"></span>
      <span class="brand__name">CORVENIX</span>
    </div>
  </section>

  <section class="card card--front" aria-label="Business card front">
    <svg class="card__bands" viewBox="0 0 700 400" aria-hidden="true">
      <path d="M0 262 Q350 280 700 322 V334 Q350 292 0 274 Z" fill="var(--blue)"/>
      <path d="M0 278 Q350 296 700 338 V400 H0 Z" fill="var(--band)"/>
    </svg>
    <div class="brand">
      <span class="brand__dot"></span>
      <span class="brand__name">CORVENIX</span>
    </div>
    <div class="person">
      <p class="person__name">Your Name</p>
      <p class="person__role">POSITION</p>
    </div>
    <ul class="contact">
      <li class="contact__item">000 000 000
        <svg class="contact__icon" viewBox="0 0 16 16" aria-hidden="true"><path d="M4 1 L6.5 4.5 L5 6 Q6.5 9.5 10 11 L11.5 9.5 L15 12 L13 15 Q4 14 1 3 Z" fill="none" stroke="var(--blue)" stroke-width="1.4"/></svg>
      </li>
      <li class="contact__item">000 000 000
        <svg class="contact__icon" viewBox="0 0 16 16" aria-hidden="true"><rect x="4" y="1" width="8" height="14" rx="1.5" fill="none" stroke="var(--blue)" stroke-width="1.4"/><rect x="5.5" y="3" width="5" height="5" fill="var(--blue)"/></svg>
      </li>
      <li class="contact__item">000@000000
        <svg class="contact__icon" viewBox="0 0 16 16" aria-hidden="true"><rect x="1" y="3" width="14" height="10" fill="none" stroke="var(--blue)" stroke-width="1.4"/><path d="M1 3 L8 9 L15 3" fill="none" stroke="var(--blue)" stroke-width="1.4"/></svg>
      </li>
      <li class="contact__item">www.0000000000
        <svg class="contact__icon" viewBox="0 0 16 16" aria-hidden="true"><path d="M3 1 L13 9 L8.5 9.5 L11 14.5 L9 15.5 L6.5 10.5 L3 13 Z" fill="none" stroke="var(--blue)" stroke-width="1.4" stroke-linejoin="round"/></svg>
      </li>
    </ul>
  </section>

</main>
</body>
</html>
```